Business Card Design Project

We need a double-sided business card design for our e-commerce company. Be as creative as you can.

Reason: Change of logo

Target Market(s)

Business owners

Industry/Entity Type

E-Commerce

Requirements
Must have
• Name (editable)
Mobile number -editable
www.trizvo.com - MUST STAND OUT ALONE
Office address:
27 Pellow Road
#09-04 Corbell Tower
Singapore 058214

```html
<!DOCTYPE html>
<html lang="en">
<head>
<meta charset="utf-8">
<title>Trizvo Business Card</title>
<link href="https://fonts.googleapis.com/css2?family=Kaushan+Script&display=swap" rel="stylesheet">
<style>
  :root {
    --card-black: #070908;
    --gap-white: #ffffff;
    --brand-orange: #ff5a12;
    --name-red: #ff3a10;
    --text-white: #ffffff;
    --stripe-orange-top: #ff3200;
    --stripe-orange-bottom: #ff5a14;
    --stripe-blue-top: #5ccbff;
    --stripe-blue-bottom: #2f7cf0;
  }
  * { margin: 0; padding: 0; box-sizing: border-box; }
  html, body {
    width: 1200px;
    height: 772px;
    overflow: hidden;
    background: var(--gap-white);
  }
  .sheet {
    position: relative;
    width: 1200px;
    height: 772px;
    font-family: "Kaushan Script", cursive;
  }
  .card-back, .card-front {
    position: absolute;
    top: 0;
    height: 772px;
    background: var(--card-black);
    overflow: hidden;
  }
  .card-back { left: 0; width: 505px; }
  .card-front { left: 695px; width: 505px; }

  .web-address {
    position: absolute;
    left: 0;
    width: 505px;
    top: 352px;
    text-align: center;
    font-size: 40px;
    line-height: 1;
    color: var(--text-white);
    white-space: nowrap;
  }
  .web-address .web-brand { color: var(--brand-orange); }

  .brand-name {
    position: absolute;
    left: 125px;
    top: 132px;
    font-size: 70px;
    line-height: 1;
    color: var(--brand-orange);
    display: flex;
    align-items: center;
    gap: 14px;
  }
  .brand-dot {
    width: 16px;
    height: 16px;
    border-radius: 50%;
    background: var(--brand-orange);
  }

  .holder-name {
    position: absolute;
    left: 125px;
    top: 266px;
    font-size: 40px;
    line-height: 60px;
    color: var(--name-red);
  }
  .contact-details {
    position: absolute;
    left: 125px;
    top: 386px;
    font-size: 16px;
    line-height: 24px;
    color: var(--name-red);
    font-style: normal;
  }
  .stripes {
    position: absolute;
    left: 0;
    top: 0;
    width: 505px;
    height: 772px;
  }
</style>
</head>
<body>
<main class="sheet">
  <section class="card-back">
    <p class="web-address">www.<span class="web-brand">trizvo</span>.com</p>
  </section>

  <section class="card-front">
    <svg class="stripes" viewBox="0 0 505 772" aria-hidden="true">
      <defs>
        <linearGradient id="stripeOrange" x1="0" y1="0" x2="0" y2="1">
          <stop offset="0" stop-color="var(--stripe-orange-top)"/>
          <stop offset="1" stop-color="var(--stripe-orange-bottom)"/>
        </linearGradient>
        <linearGradient id="stripeBlue" x1="1" y1="0" x2="0" y2="1">
          <stop offset="0" stop-color="var(--stripe-blue-top)"/>
          <stop offset="1" stop-color="var(--stripe-blue-bottom)"/>
        </linearGradient>
      </defs>
      <polygon points="125,497 327,497 52,772 0,772 0,622" fill="url(#stripeOrange)"/>
      <polygon points="505,355 505,560 293,772 90,772" fill="url(#stripeBlue)"/>
    </svg>

    <div class="brand-name">Trizvo<span class="brand-dot"></span></div>

    <h1 class="holder-name">Marcus<br>Holden</h1>

    <address class="contact-details">
      +65-8734-219-05<br>
      27 Pellow Road<br>
      #09-04 Corbell Tower<br>
      Singapore 058214
    </address>
  </section>
</main>
</body>
</html>
```